Website that needs to be finished

I'm looking for someone who is a MASTER at Wordpress and can finish off a website that was started by others. I need a professional builder who knows exactly how it's done with a strong knowledge of marketing and English Language copy skills. We are looking for someone well established who has built at least 40 other websites. It needs to be a modern version of our existing website at www.falconworksgroup.example

Target Market(s)

Commercial roofing website re-do

Contact Information for Business Card

same branding as website on custom paper

Coding

Coded - Design and coding required

Number of Pages Required

5+ page

Font styles to use
Other font styles liked:
• Gilroy Standard

Colors
3377b5

Requirements
Must have
• same color, Same look, better quality photos, faster

```html
<!DOCTYPE html>
<html lang="en">
<head>
<meta charset="utf-8">
<title>Falconworks Roofing — Commercial Roofing Denver</title>
<link href="https://fonts.googleapis.com/css2?family=Outfit:wght@300;400;500;600;700;800&display=swap" rel="stylesheet">
<style>
:root{
  --brand:#3377b5;
  --brand-deep:#2d6aa6;
  --ink:#222222;
  --text:#666666;
  --white:#ffffff;
  --footer:#f6f6f6;
  --black:#141414;
}
*{box-sizing:border-box;margin:0;padding:0}
html,body{width:1200px;height:2912px;overflow:hidden}
body{font-family:"Outfit",sans-serif;color:var(--ink);background:var(--white);position:relative}
a{color:inherit;text-decoration:none}
.section{position:absolute;left:0;width:1200px}

/* top bar */
.topbar{top:0;height:60px;background:var(--brand);color:var(--white)}
.topbar .item{position:absolute;top:0;height:60px;display:flex;align-items:center;gap:12px}
.topbar .phone{left:113px;font-size:21px;font-weight:700}
.topbar .address{left:464px;font-size:16px;font-weight:300}
.social{position:absolute;right:112px;top:18px;display:flex;gap:14px}
.social span{width:27px;height:27px;border:1.5px solid var(--white);display:block}

/* nav */
.nav{top:60px;height:100px;background:var(--white)}
.brand{position:absolute;left:110px;top:33px;display:flex;align-items:center;gap:10px;font-size:28px;font-weight:700;color:var(--brand)}
.brand .mark{width:26px;height:26px;background:var(--brand);border-radius:50%}
.menu{position:absolute;left:0;top:0;width:1200px;height:100px;font-size:15.5px;color:#333}
.menu a{position:absolute;top:0;height:100px;display:flex;align-items:center;white-space:nowrap}
.menu .active{color:var(--brand)}
.menu .caret{gap:4px}
.btn{display:inline-flex;align-items:center;justify-content:center;font-weight:700;border-radius:6px;font-size:15px}
.btn-book{position:absolute;left:933px;top:25px;width:155px;height:52px;background:var(--brand);color:var(--white)}

/* hero */
.hero{top:160px;height:556px;background:linear-gradient(160deg,#8b8f93 0%,#6f7275 40%,#9a9894 75%,#bdb9b2 100%)}
.hero-circle{position:absolute;left:113px;top:54px;width:446px;height:446px;border-radius:50%;background:var(--white);padding:8px}
.hero-circle .inner{width:100%;height:100%;border-radius:50%;background:rgba(51,119,181,.93);color:var(--white);text-align:center;padding-top:96px}
.hero-circle h1{font-size:38px;font-weight:800;line-height:52px}
.hero-circle p{font-size:16px;font-weight:300;line-height:33px;margin-top:10px}
.btn-light{background:var(--white);color:var(--brand);width:154px;height:51px;margin-top:20px}
.arrow{position:absolute;top:262px}

/* about */
.about{top:716px;height:628px}
.about h2{position:absolute;left:110px;top:92px;width:540px;font-size:30px;font-weight:800;line-height:52px;white-space:nowrap}
.about p{position:absolute;left:110px;top:255px;width:470px;font-size:15.5px;line-height:33.4px;color:var(--text);font-weight:300;text-align:justify;letter-spacing:.35px}
.btn-primary{position:absolute;left:111px;top:473px;width:309px;height:51px;background:var(--brand);color:var(--white)}
.about-photo{position:absolute;left:632px;top:102px;width:457px;height:423px;border:5px solid var(--white);box-shadow:0 0 6px rgba(0,0,0,.18);background:linear-gradient(135deg,#c9d6e0 0%,#6a7c8c 50%,#3c4652 100%)}

/* systems */
.systems{top:1344px;height:456px;background:var(--brand);color:var(--white);text-align:center}
.systems h2{font-size:41px;font-weight:800;padding-top:58px}
.systems ul{list-style:none;display:flex;justify-content:center;gap:42px;font-size:20px;font-weight:700;margin-top:22px}
.systems p{width:970px;margin:26px auto 0;font-size:16px;line-height:35px;font-weight:300}
.systems .btn-light{margin-top:20px}

/* services */
.services{top:1800px;height:590px}
.services h2{text-align:center;font-size:41px;font-weight:800;padding-top:96px}
.cards{position:absolute;top:178px;left:110px;display:flex;gap:12px}
.card{position:relative;width:318px;height:303px;border:4px solid var(--white);box-shadow:0 0 5px rgba(0,0,0,.18);overflow:hidden;color:var(--white);text-align:center;padding:74px 12px 0}
.card.c1{background:linear-gradient(160deg,#5a4630,#2a2520 70%)}
.card.c2{background:linear-gradient(160deg,#4a5360,#2a3038 70%)}
.card.c3{background:linear-gradient(160deg,#6a5a50,#3a3c40 70%)}
.card .stripe{position:absolute;right:-10px;top:-30px;width:30px;height:170px;background:var(--brand);transform:rotate(-38deg);transform-origin:top center}
.card h3{font-size:21px;font-weight:700;position:relative}
.card h3 span{color:var(--brand)}
.card p{font-size:14px;line-height:30px;margin-top:10px;font-weight:300}
.card a{display:inline-block;margin-top:2px;font-size:15px;font-weight:700;color:var(--brand);text-decoration:underline}

/* cta */
.cta{top:2390px;height:342px;background:linear-gradient(150deg,#6e7275 0%,#85878a 45%,#a7a6a2 100%);color:var(--white);text-align:center}
.cta h2{font-size:26px;font-weight:700;padding-top:88px}
.cta .big-phone{font-size:42px;font-weight:700;margin-top:14px}
.btn-dark{background:var(--black);color:var(--white);width:189px;height:51px;margin-top:16px}

/* footer */
.footer{top:2732px;height:180px;background:var(--footer);text-align:center;color:#333}
.footer nav{margin-top:38px;font-size:16px;display:flex;justify-content:center;gap:22px}
.footer nav .sep{color:#777}
.footer .meta{font-size:15.5px;margin-top:20px}
.footer .copy{font-size:15px;margin-top:20px}
</style>
</head>
<body>

<header class="section topbar">
  <div class="item phone">
    <svg width="32" height="32" viewBox="0 0 32 32" fill="none" stroke="#fff" stroke-width="1.3"><circle cx="16" cy="16" r="15"/><path d="M11 9l3 3-2 2c1 2 3 4 5 5l2-2 3 3-2 2c-5 0-11-6-11-11z"/></svg>
    <span>555.014.0866</span>
  </div>
  <div class="item address">
    <svg width="32" height="32" viewBox="0 0 32 32" fill="none" stroke="#fff" stroke-width="1.3"><circle cx="16" cy="16" r="15"/><path d="M16 24s-6-6-6-10a6 6 0 0112 0c0 4-6 10-6 10z"/><circle cx="16" cy="14" r="2"/></svg>
    <span>1480 S. Alder StEnglewood, CO 80110</span>
  </div>
  <div class="social" aria-label="Social links"><span></span><span></span><span></span></div>
</header>

<nav class="section nav">
  <div class="brand"><span class="mark"></span>Falconworks</div>
  <div class="menu">
    <a class="active" style="left:415px">HOME</a>
    <a style="left:489px">ABOUT</a>
    <a class="caret" style="left:570px">SERVICES <svg width="12" height="8" viewBox="0 0 12 8" fill="none" stroke="#333" stroke-width="1.5"><path d="M1 1l5 5 5-5"/></svg></a>
    <a style="left:674px">GALLERY</a>
    <a style="left:768px">NEWS</a>
    <a style="left:842px">CONTACT</a>
  </div>
  <a class="btn btn-book">BOOK ONLINE</a>
</nav>

<section class="section hero" role="img" aria-label="Aerial photo of a flat commercial roof with HVAC units">
  <svg class="arrow" style="left:70px" width="20" height="34" viewBox="0 0 20 34" fill="none" stroke="#fff" stroke-width="2"><path d="M18 1L2 17l16 16"/></svg>
  <svg class="arrow" style="left:1104px" width="20" height="34" viewBox="0 0 20 34" fill="none" stroke="#fff" stroke-width="2"><path d="M2 1l16 16L2 33"/></svg>
  <div class="hero-circle">
    <div class="inner">
      <h1>QUALITY<br>ROOFING SERVICES</h1>
      <p>Falconworks Roofing has been satisfying customers with<br>challenging roofing issues for over 25 years.</p>
      <a class="btn btn-light">GET STARTED</a>
    </div>
  </div>
</section>

<section class="section about">
  <h2>QUALITY COMMERCIAL ROOFING<br>REPAIR &amp; ROOFING REPLACEMENT<br>IN DENVER.</h2>
  <p>Falconworks Roofing has been satisfying owners with challenging roofing issues for over 25 years in the Colorado front-range region. From rehabbing persistent damaging leaks to complete new commercial roofing systems, Falconworks Roofing is an authorized installer for some of the most trusted roofing system manufacturers world wide. With millions</p>
  <a class="btn btn-primary">SCHEDULE AN APPOINTMENT ONLINE</a>
  <div class="about-photo" role="img" aria-label="Photo of two roofers in hard hats working on a shingle roof"></div>
</section>

<section class="section systems">
  <h2>ROOFING SYSTEMS</h2>
  <ul><li>EPDM</li><li>TPO</li><li>PVC</li><li>POLYUREA</li><li>MODIFIED</li></ul>
  <p>Located in Morrison and Englewood CO, Falconworks Roofing specializes in cost engineering complicated commercial roofing systems. Just because a roof may leak, doesn't mean that it always needs to be replaced. In fact, even well-constructed roofing systems will leak during certain storm events, often due to a simple problem. It takes a trained eye to inspect a roof properly and incorporate a detail to resolve that roofing condition.</p>
  <a class="btn btn-light">READ MORE</a>
</section>

<section class="section services">
  <h2>OUR SERVICES</h2>
  <div class="cards">
    <article class="card c1" role="img" aria-label="Photo of a roofer working on a commercial roof">
      <div class="stripe"></div>
      <h3><span>COMMERCIAL</span> ROOFING</h3>
      <p>Commercial building roofs have a hard life and when they need to be replaced, we'll put on a new one that is trouble free and that will last.</p>
      <a>LEARN MORE</a>
    </article>
    <article class="card c2" role="img" aria-label="Photo of a custom family home at dusk">
      <div class="stripe"></div>
      <h3><span>CUSTOM</span> HOMES</h3>
      <p>Serious leaks around chimneys, drains, gutters, valleys need to get addressed and we know how to fix them all.</p>
      <a>LEARN MORE</a>
    </article>
    <article class="card c3" role="img" aria-label="Photo of a roofer laying roof tiles">
      <div class="stripe"></div>
      <h3><span>ROOFING</span> SERVICES</h3>
      <p>Sagging ceiling tiles, damp carpets, stained drywall are all signs you need to fix your roof – we can find and seal any problem quickly and efficiently.</p>
      <a>LEARN MORE</a>
    </article>
  </div>
</section>

<section class="section cta" role="img" aria-label="Photo of a flat commercial roof with rooftop equipment">
  <h2>CONTACT US TODAY TO GET A CONSULTATION!</h2>
  <div class="big-phone">555.014.0866</div>
  <a class="btn btn-dark">BOOK ONLINE</a>
</section>

<footer class="section footer">
  <nav>
    <a>HOME</a><span class="sep">/</span><a>ABOUT</a><span class="sep">/</span><a>SERVICES</a><span class="sep">/</span><a>GALLERY</a><span class="sep">/</span><a>NEWS</a><span class="sep">/</span><a>CONTACT</a>
  </nav>
  <div class="meta">Sitemap | Sitemap xml | Rss feed | Sign in</div>
  <div class="copy">© 2020 All Rights Reserved</div>
</footer>

</body>
</html>
```